Alborada Fondos Invest - 2018 Website

We are an investment platform based in Madrid, Spain, that focuses on buying companies to improve them operationally and ignite growth through modernization, digitalization and a real hands on approach in the management of those companies we buy. We want to become a serious player in the private equity and money management industry and start approaching more institutional investors (such as pension funds, large family offices, etc.) in the coming months for an intense fundraising campaign.

For such purpose, we need a professional website with an impeccable design and streamlined communication. While we do want to provide some details in terms of what we do, who we are, our investment strategy, etc. we also want to be as vague as possible so that we do not limit ourselves to the claims we do on the website in terms of kind of investments, sectors, industries, geographies, etc. that we work on. For now we raise capital on a deal by deal basis, although our goal is to raise a discretionary pool of capital that we would deploy over 3-5 years. We are now building our track record as a team with already 2 investments which are showing massive growth potential and for which we have been able to execute the investment thesis as planned so far.

We need a simple and clear website with an incredibly professional image to go on the above mentioned roadshow and meet institutional investors.

For reference, we believe the following investment funds have very nice websites:

1) Brezo Private Equity - http://brezoequity-example.com/
2) Valdemar Capital - http://www.valdemarcapital-example.es/
3) Tresaco Capital - https://www.tresacocapital-example.com/

Thank you in advance.
Tomás Ribera Salcedo

Target Market(s)

Potential professional investors - from High Net Worth individuals, to more institutional investors such as Family Offices, Investment Funds, Pension Funds, etc.

Contact Information for Business Card

Name
Title
Contact Details (only for Andrés Villar Oña and Tomás Ribera Salcedo)

Font styles to use
Sans Serif

Colors

Designer to choose colors to be used in the design.

```html
<!DOCTYPE html>
<html lang="en">
<head>
<meta charset="utf-8">
<title>Alborada Fondos Invest</title>
<link rel="stylesheet" href="https://fonts.googleapis.com/css2?family=Montserrat:wght@400;500;600&family=Open+Sans:wght@400;600&display=swap">
<style>
:root{
  --navy:#2b2947;
  --navy-deep:#232140;
  --ink:#2f2f3a;
  --text:#5a5a66;
  --muted:#8a8a94;
  --line:#b9b9c4;
  --light:#f3f3f3;
  --slant:#d4d4d6;
  --white:#ffffff;
}
*{box-sizing:border-box;margin:0;padding:0}
html,body{width:1200px;height:3237px;overflow:hidden;background:var(--white)}
body{position:relative;font-family:"Open Sans",Arial,sans-serif;color:var(--text)}
.abs{position:absolute}
h1,h2,h3,.brand,.nav a{font-family:"Montserrat",Arial,sans-serif}

/* header */
.brand{left:135px;top:36px;display:flex;align-items:center;gap:14px;color:var(--navy);font-size:30px;font-weight:500;letter-spacing:2px}
.brand .mark{width:26px;height:26px;background:var(--navy)}
.social{top:36px;left:786px;display:flex;gap:14px}
.social span{width:14px;height:14px;border-radius:50%;background:#77778a}
.lang{left:858px;top:25px;width:90px;height:32px;border:1px solid #ccc;font-size:11px;padding:8px 10px;color:#555}
.lang::after{content:"";position:absolute;right:10px;top:13px;border:4px solid transparent;border-top-color:#555}
.login{left:963px;top:25px;width:104px;height:32px;border:1px solid #ccc;font-size:11px;padding:8px 10px;color:#555}
.nav{top:80px;right:133px;display:flex;gap:28px}
.nav a{font-size:13px;color:#333;text-decoration:none}
.nav a.active{font-weight:600}

/* hero */
.hero{left:0;top:122px;width:1200px;height:493px;background:linear-gradient(120deg,#e9c9a0 0%,#b58d6b 25%,#6f6660 55%,#3a3a44 100%)}
.hero-title{left:0;top:484px;width:1200px;text-align:center;color:#eee;font-family:"Montserrat",Arial,sans-serif;font-size:38px;font-weight:500;letter-spacing:1px}
.arrow{top:352px;width:22px;height:30px}

/* welcome */
.welcome-frame{left:140px;top:713px;width:326px;height:283px;background:var(--slant);transform:skewY(2deg)}
.welcome-photo{left:132px;top:738px;width:334px;height:282px;background:linear-gradient(135deg,#c9a680,#9aa3ad 50%,#e8e8ea)}
.h-section{font-size:40px;font-weight:400;color:var(--ink);letter-spacing:1px}
.welcome-h{left:495px;top:724px}
.welcome-p{left:495px;top:790px;width:572px;font-size:14.5px;line-height:26px}
.welcome-p p+p{margin-top:26px}

/* feature cards */
.features{left:0;top:1178px;width:1200px;height:420px;background:var(--light)}
.card{top:1243px;width:301px;height:292px;border:1px solid #9a9aae;background:var(--white);text-align:center;padding-top:30px}
.card svg{width:56px;height:56px;stroke:var(--navy);fill:none;stroke-width:2}
.card h3{font-size:17px;font-weight:400;color:var(--ink);margin-top:10px}
.card p{font-size:10.5px;line-height:18px;color:#555;margin:10px auto 0;width:250px;height:66px}
.btn-more{position:absolute;left:50%;top:226px;transform:translateX(-50%);width:97px;height:34px;border:1px solid #777;font-size:10px;line-height:32px;color:#333}

/* strategy */
.strategy-h{left:132px;top:1788px}
.strategy-list{left:132px;top:1852px;list-style:none;font-size:19px;color:var(--ink)}
.strategy-list li{height:40px;display:flex;align-items:center;gap:12px}
.strategy-list li::before{content:"";width:7px;height:7px;border-right:1.5px solid #333;border-top:1.5px solid #333;transform:rotate(45deg)}
.strategy-frame{left:741px;top:1735px;width:326px;height:283px;background:var(--slant);transform:skewY(2deg)}
.strategy-photo{left:733px;top:1760px;width:334px;height:282px;background:linear-gradient(180deg,#e4eef4 0%,#c7d6e0 45%,#7fa9c2 70%,#5b8fae 100%)}

/* what we do */
.services{left:0;top:2229px;width:1200px;height:372px;background:var(--navy)}
.services-h{left:0;top:2306px;width:1200px;text-align:center;color:var(--white)}
.service{top:2376px;width:134px;height:138px;border:1px solid #7c7a98;text-align:center;color:#ddd;font-size:13px;line-height:17px;padding-top:16px}
.service svg{width:50px;height:50px;stroke:#e4e4ee;fill:none;stroke-width:1.8;display:block;margin:0 auto 10px}

/* contact */
.contact-h{left:0;top:2726px;width:1200px;text-align:center}
.field{top:2795px;height:40px;border:1px solid #ccc;font-size:11px;color:#999;padding:12px 10px}
.submit{left:563px;top:2925px;width:74px;height:40px;background:var(--navy);color:var(--white);font-size:11px;text-align:center;line-height:40px;font-weight:600}

/* footer */
.footer{left:0;top:3110px;width:1200px;height:127px;background:var(--navy)}
.footer-links{left:132px;top:3151px;font-size:10.5px;color:#c9c9d8}
.footer-copy{left:132px;top:3179px;font-size:10.5px;color:#c9c9d8}
.to-top{left:1030px;top:3154px;width:36px;height:36px;border-radius:50%;background:#6e6c8e}
</style>
</head>
<body>

<header>
  <div class="abs brand"><span class="mark"></span>ALBORADA FONDOS</div>
  <div class="abs social"><span></span><span></span></div>
  <div class="abs lang">English</div>
  <div class="abs login">&#8594; Investor Login</div>
  <nav class="abs nav">
    <a class="active" href="#">Welcome</a><a href="#">About</a><a href="#">Opportunities</a><a href="#">Investment Strategy</a><a href="#">Our Team</a><a href="#">Contact</a>
  </nav>
</header>

<section>
  <div class="abs hero" role="img" aria-label="Photo of a businessman signing a document at a desk"></div>
  <svg class="abs" style="left:0;top:540px" width="1200" height="120" viewBox="0 0 1200 120">
    <polygon points="0,10 1200,75 1200,115 1140,115 0,75" fill="var(--slant)"/>
    <polygon points="0,10 1200,52 1200,75 0,75" fill="var(--navy)"/>
  </svg>
  <h1 class="abs hero-title">MAURIS BIBENDUM FRINGILLA</h1>
  <svg class="abs arrow" style="left:46px" viewBox="0 0 22 30"><polyline points="16,4 5,15 16,26" fill="none" stroke="#fff" stroke-width="3"/></svg>
  <svg class="abs arrow" style="left:1132px" viewBox="0 0 22 30"><polyline points="6,4 17,15 6,26" fill="none" stroke="#fff" stroke-width="3"/></svg>
</section>

<section>
  <div class="abs welcome-frame"></div>
  <div class="abs welcome-photo" role="img" aria-label="Photo of a laptop and tablet showing charts on a desk"></div>
  <h2 class="abs h-section welcome-h">WELCOME</h2>
  <div class="abs welcome-p">
    <p>Alborada Fondos Invest is a unique investment platform focused on value creation through consolidation, digitalization and internationalization of large, fragmented and traditional sectors. We build platforms and ecosystems, and ignite organic and inorganic growth in plateauing industries</p>
    <p>Weldo so by applying a true hands-on approach and deep involvement in operations throughout the life of the investment, and by rigorously analysing the sectors we invest in. We believe that above-market returns can only be unlocked through deep understanding of the day to day affairs of our businesses</p>
  </div>
</section>

<section>
  <svg class="abs" style="left:0;top:1115px" width="1200" height="65" viewBox="0 0 1200 65"><polygon points="0,65 1185,0 1200,65" fill="var(--navy)"/></svg>
  <div class="abs features"></div>
  <svg class="abs" style="left:0;top:1597px" width="1200" height="45" viewBox="0 0 1200 45"><polygon points="0,0 1200,0 1200,3 20,45 10,45" fill="var(--slant)"/></svg>

  <div class="abs card" style="left:132px">
    <svg viewBox="0 0 56 56"><path d="M4 22l10-8 10 4 8-4 10 2 10 8M14 14l-8 14 16 14 6-4M42 16l8 14-16 14-6-4M22 32l6 5M26 28l6 5M30 24l6 5"/></svg>
    <h3>THE OPPORTUNITY</h3>
    <p>Substantial investment opportunities in the low-mid market in Spain exist thanks to:<br>&bull; Highly fragmented industry with a very high number of SMEs</p>
    <div class="btn-more">READ MORE</div>
  </div>
  <div class="abs card" style="left:449px">
    <svg viewBox="0 0 56 56"><rect x="8" y="6" width="40" height="44"/><circle cx="22" cy="22" r="8"/><path d="M22 14v8h8M34 16h10M34 22h10M34 28h10M14 38h30M14 44h30"/></svg>
    <h3>THE PLATFORM</h3>
    <p>Alborada Fondos Invest focuses on mature and stable assets but that present a growth opportunity if some levers are utilized (large scale consolidations, fresh management, internationalization, growth</p>
    <div class="btn-more">READ MORE</div>
  </div>
  <div class="abs card" style="left:766px">
    <svg viewBox="0 0 56 56"><rect x="14" y="6" width="28" height="46"/><path d="M20 12h5v5h-5zM31 12h5v5h-5zM20 22h5v5h-5zM31 22h5v5h-5zM20 32h5v5h-5zM31 32h5v5h-5zM24 52v-8h8v8M6 52h44"/></svg>
    <h3>COMPETITIVE ADVANTAGE</h3>
    <p>A true hands-on approach and deep involvement in operations<br>Deep know-how and expertise navigating local market</p>
    <div class="btn-more">READ MORE</div>
  </div>
</section>

<section>
  <h2 class="abs h-section strategy-h">MAECENAS VEL</h2>
  <ul class="abs strategy-list">
    <li>How do we Source Deals?</li>
    <li>How do we Create Value?</li>
    <li>How do we Exit Investments?</li>
    <li>How do we differentiate ourselves?</li>
  </ul>
  <div class="abs strategy-frame"></div>
  <div class="abs strategy-photo" role="img" aria-label="Photo of a businessman seen from behind looking at a marina with sailboats"></div>
</section>

<section>
  <svg class="abs" style="left:0;top:2165px" width="1200" height="65" viewBox="0 0 1200 65"><polygon points="0,65 15,0 1200,55 1200,65" fill="var(--slant)"/></svg>
  <div class="abs services"></div>
  <svg class="abs" style="left:0;top:2600px" width="1200" height="42" viewBox="0 0 1200 42"><polygon points="0,0 1200,0 1200,42 1170,42 0,14" fill="#4a4a52"/></svg>
  <h2 class="abs h-section services-h">WHAT WE DO</h2>

  <div class="abs service" style="left:132px"><svg viewBox="0 0 50 50"><path d="M6 44h38M10 44V34h6v10M20 44V28h6v16M30 44V20h6v24M40 44V12"/><path d="M8 26l12-10 8 6 16-14M38 8h6v6"/></svg>Private Equity</div>
  <div class="abs service" style="left:294px"><svg viewBox="0 0 50 50"><path d="M6 44h38M10 44V32h6v12M20 44V26h6v18M30 44V20h6v24"/><circle cx="38" cy="12" r="7"/><path d="M38 8v8"/></svg>Money<br>Management</div>
  <div class="abs service" style="left:454px"><svg viewBox="0 0 50 50"><circle cx="25" cy="20" r="11"/><path d="M25 14v12M22 17h5M22 23h5M6 40h12l6 4 14-6M6 36h10"/></svg>Institutional<br>Investors</div>
  <div class="abs service" style="left:614px"><svg viewBox="0 0 50 50"><circle cx="22" cy="10" r="4"/><path d="M22 16v14l-6 14M22 30l4 14M22 20l-8 6M22 20l8 4 2 20"/></svg>Pension Funds</div>
  <div class="abs service" style="left:774px"><svg viewBox="0 0 50 50"><rect x="10" y="8" width="16" height="36"/><rect x="26" y="18" width="14" height="26"/><path d="M14 14h3M20 14h3M14 22h3M20 22h3M14 30h3M20 30h3M30 24h3M30 32h3M6 44h38"/></svg>Large Family<br>Offices</div>
  <div class="abs service" style="left:934px"><svg viewBox="0 0 50 50"><circle cx="28" cy="16" r="9"/><path d="M28 11v10M25 14h5M25 18h5M6 38h12l8 4 16-8M6 32h12l6 2"/></svg>Fundraising<br>Campaign</div>
</section>

<section>
  <h2 class="abs h-section contact-h">CONTACT US</h2>
  <div class="abs field" style="left:132px;width:217px">First Name</div>
  <div class="abs field" style="left:373px;width:216px">Last Name</div>
  <div class="abs field" style="left:614px;width:214px">Phone Number</div>
  <div class="abs field" style="left:850px;width:217px">Email Address</div>
  <div class="abs field" style="left:132px;top:2860px;width:935px">Message</div>
  <div class="abs submit">SUBMIT</div>
</section>

<footer>
  <svg class="abs" style="left:0;top:3045px" width="1200" height="66" viewBox="0 0 1200 66"><polygon points="0,66 1190,0 1200,66" fill="#e6e6e8"/></svg>
  <div class="abs footer"></div>
  <div class="abs footer-links">Welcome &nbsp;|&nbsp; About &nbsp;|&nbsp; Opportunities &nbsp;|&nbsp; Investment Strategy &nbsp;|&nbsp; Our Team &nbsp;|&nbsp; Contact</div>
  <div class="abs footer-copy">Copyright &copy; 2018 Alborada Fondos Invest. &nbsp;All rights reserved.</div>
  <div class="abs to-top"><svg width="36" height="36" viewBox="0 0 36 36"><polyline points="11,21 18,14 25,21" fill="none" stroke="#fff" stroke-width="3"/></svg></div>
</footer>

</body>
</html>
```